" distribuidora no ramo do atacado e varejo (loja fisica ) nos produtos de embalagens em geral (descartáveis, festas e etc.) produtos de limpezas para (residencias , comércios e industriais ) e produtos personalizados no mesmo ramo. "

```html
<!DOCTYPE html>
<html lang="pt-BR">
<head>
<meta charset="utf-8">
<title>Valmora Distribuidora – Porta-copos</title>
<link href="https://fonts.googleapis.com/css2?family=Exo+2:wght@400;600;800&display=swap" rel="stylesheet">
<style>
  :root {
    --page-bg: #eef0f1;
    --coaster-white: #ffffff;
    --ring-blue: #1f7ea6;
    --brand-grey: #7b7f84;
    --brand-dark: #55595e;
    --contact-blue: #1d5fa8;
    --mark-green: #7cc242;
  }
  * { margin: 0; padding: 0; box-sizing: border-box; }
  html, body {
    width: 1200px;
    height: 1200px;
    overflow: hidden;
    background: var(--page-bg);
    font-family: "Exo 2", sans-serif;
  }
  .canvas {
    width: 1200px;
    height: 1200px;
    display: flex;
    align-items: center;
    justify-content: center;
  }
  .coaster {
    position: relative;
    width: 1000px;
    height: 1000px;
    border-radius: 50%;
    background: var(--coaster-white);
    box-shadow: 0 6px 24px rgba(0,0,0,0.08);
    display: flex;
    flex-direction: column;
    align-items: center;
  }
  .coaster-ring {
    position: absolute;
    inset: 22px;
    border-radius: 50%;
    border: 12px solid var(--ring-blue);
  }
  .brand-mark {
    margin-top: 120px;
    width: 190px;
    height: 190px;
    border-radius: 50%;
    background: var(--mark-green);
  }
  .brand-name {
    margin-top: 40px;
    font-weight: 800;
    font-size: 118px;
    line-height: 1;
    letter-spacing: 4px;
    color: var(--brand-grey);
  }
  .brand-tagline {
    margin-top: 14px;
    font-weight: 400;
    font-size: 32px;
    letter-spacing: 14px;
    padding-left: 14px;
    color: var(--brand-dark);
  }
  .contact {
    margin-top: 70px;
    text-align: center;
    color: var(--contact-blue);
    font-weight: 600;
  }
  .contact-phone {
    font-size: 34px;
    letter-spacing: 1px;
  }
  .contact-site {
    margin-top: 18px;
    font-size: 30px;
    letter-spacing: 10px;
    padding-left: 10px;
  }
</style>
</head>
<body>
  <main class="canvas">
    <section class="coaster">
      <div class="coaster-ring"></div>
      <div class="brand-mark"></div>
      <h1 class="brand-name">VALMORA</h1>
      <p class="brand-tagline">DISTRIBUIDORA</p>
      <div class="contact">
        <p class="contact-phone">11 55555-0000</p>
        <p class="contact-site">www.valmora.com.br</p>
      </div>
    </section>
  </main>
</body>
</html>
```